Business Cards for cafe providing speciality coffee and food

I need a business card design for my husband’s businesses. He has two cafes in Brisbane. The business name is Copperleaf Roasting House. They sell high end specialty coffee as well as breakfast and lunch. All the food is cooked fresh, in house and they have strict quality controls for their coffee. I would like the business card to feature the address for both cafes, my husband’s phone number and the business’s instagram. The address for the first is 61 Wexley Crescent, Pine Hollow and the second is 23 Dorrit Avenue, Sallowmere. The Instagram handle is @copperleafroastinghouse and phone number is 0491326085. We already have a business logo that is attached.

Target Market(s)

All ages, higher disposable income and more likely to eat out regularly

Industry/Entity Type

Hospitality

Contact Information for Business Card

Must be suitable for both customers and suppliers

Font styles to use
Sans Serif

Colors

Designer to choose colors to be used in the design.

Requirements
Must have
• Owner’s name: Griff Tallant
• Addresses of both cafes: 61 Wexley Crescent, Pine Hollow and 23 Dorrit Avenue, Sallowmere
• Instagram handle: @copperleafroastinghouse
• Contact number: 0491326085
Nice to have
• Business logo

```html
<!DOCTYPE html>
<html lang="en">
<head>
<meta charset="utf-8">
<title>Copperleaf Roasting House – Business Card</title>
<link rel="stylesheet" href="https://fonts.googleapis.com/css2?family=Oswald:wght@300;400;500;600&display=swap">
<style>
  :root {
    --bg: #5a5a5a;
    --card-dark: #1e1e1e;
    --card-dark-mark: #3a3a3a;
    --card-dark-ink: #8a8a8a;
    --card-light: #f2f2f2;
    --ink: #1a1a1a;
    --ink-soft: #2c2c2c;
  }
  * { box-sizing: border-box; margin: 0; padding: 0; }
  html, body {
    width: 1200px; height: 1021px; overflow: hidden;
    background: var(--bg);
    font-family: "Oswald", sans-serif;
  }
  .canvas {
    width: 1200px; height: 1021px;
    display: flex; flex-direction: column; align-items: center; justify-content: center;
    gap: 50px;
  }
  .card {
    width: 760px; height: 434px; position: relative;
    box-shadow: 0 14px 30px rgba(0,0,0,.35);
  }
  /* Front face */
  .card--front {
    background: var(--card-dark);
    display: flex; align-items: center; justify-content: center;
  }
  .brand-mark {
    width: 250px; height: 250px; border-radius: 50%;
    border: 6px solid var(--card-dark-mark);
    display: flex; align-items: center; justify-content: center;
    text-align: center;
  }
  .brand-name {
    font-weight: 500; text-transform: uppercase;
    font-size: 24px; line-height: 1.25; letter-spacing: 2px;
  }
  .card--front .brand-name { color: var(--card-dark-ink); }

  /* Back face */
  .card--back {
    background: var(--card-light);
    display: flex; align-items: center;
  }
  .card--back .brand-mark {
    width: 230px; height: 230px;
    border-color: var(--ink);
    margin-left: 70px;
  }
  .card--back .brand-name { color: var(--ink); font-size: 22px; }
  .contact {
    margin-left: 90px; color: var(--ink);
  }
  .contact__name {
    font-weight: 600; font-size: 30px; letter-spacing: 1px; text-transform: uppercase; line-height: 1.1;
  }
  .contact__role {
    font-weight: 400; font-size: 17px; text-transform: uppercase; letter-spacing: 1px; color: var(--ink-soft);
  }
  .contact__rule {
    width: 34px; height: 3px; background: var(--ink); margin: 14px 0 22px;
  }
  .contact__line {
    font-weight: 300; font-size: 20px; line-height: 1.35; color: var(--ink-soft);
    display: flex; align-items: center; gap: 10px;
  }
  .contact__line svg { width: 16px; height: 16px; flex: none; }
  .contact__gap { height: 6px; }
</style>
</head>
<body>
<main class="canvas">
  <section class="card card--front" aria-label="Card front">
    <div class="brand-mark">
      <span class="brand-name">Copperleaf<br>Roasting House</span>
    </div>
  </section>

  <section class="card card--back" aria-label="Card back">
    <div class="brand-mark">
      <span class="brand-name">Copperleaf<br>Roasting House</span>
    </div>
    <div class="contact">
      <p class="contact__name">Griff Tallant</p>
      <p class="contact__role">Owner</p>
      <div class="contact__rule"></div>
      <p class="contact__line">61 Wexley Crescent, Pine Hollow</p>
      <p class="contact__line">23 Dorrit Avenue, Sallowmere</p>
      <div class="contact__gap"></div>
      <p class="contact__line">
        <svg viewBox="0 0 24 24" aria-hidden="true"><path fill="#1a1a1a" d="M6.6 10.8a15.1 15.1 0 0 0 6.6 6.6l2.2-2.2c.3-.3.7-.4 1-.2 1.1.4 2.3.6 3.6.6.6 0 1 .4 1 1V20c0 .6-.4 1-1 1C10.6 21 3 13.4 3 4c0-.6.4-1 1-1h3.5c.6 0 1 .4 1 1 0 1.3.2 2.5.6 3.6.1.3 0 .7-.2 1z"/></svg>
        0491326085
      </p>
      <p class="contact__line">@copperleafroastinghouse</p>
    </div>
  </section>
</main>
</body>
</html>
```